A Recruitment Company Needs a Web Design that Expresses High Energy and Results

Our company, BrightLane Consultants, needs a web design for our recruiting business based in Asia (Taiwan). We provide recruitment services to many international companies. Our client base is as follows:
Hi-Tech - 60%
Healthcare and Consumer/FMCG - 15%
Industrial and Engineering - 15%
Banking and Finance - 10%

The website will be accessed by both clients and job seekers. As such, it should look professional, user-friendly and is interactive.

Sans Serif

add136
ffffff
000000

• Attached is the company's logo. the design mus be in line with it.

```html
<!DOCTYPE html>
<html lang="en">
<head>
<meta charset="utf-8">
<title>BrightLane Consultants</title>
<link rel="stylesheet" href="https://fonts.googleapis.com/css2?family=Montserrat:wght@400;500;600;700&family=Open+Sans:wght@400;600&display=swap">
<style>
:root{
  --green:#add136;
  --green-dark:#95b82a;
  --white:#ffffff;
  --black:#000000;
  --ink:#1e1e1e;
  --text:#8a8a8a;
  --header-bg:#f7f7f7;
  --dark:#1f2327;
}
*{margin:0;padding:0;box-sizing:border-box}
html,body{width:819px;height:1200px;overflow:hidden;background:var(--white)}
body{position:relative;font-family:"Open Sans",Arial,sans-serif;color:var(--text)}
.abs{position:absolute}
.heading{font-family:"Montserrat",Arial,sans-serif}

/* header */
.site-header{left:0;top:0;width:819px;height:66px;background:var(--header-bg);border-bottom:1px solid #e6e6e6}
.brand{left:68px;top:20px;display:flex;align-items:center;gap:7px}
.brand-dot{width:14px;height:14px;border-radius:50%;background:var(--green)}
.brand-name{font-family:"Montserrat",Arial,sans-serif;font-weight:700;font-size:17px;color:var(--green);letter-spacing:-.2px}
.main-nav{top:28px;left:317px;display:flex;gap:0;font-family:"Montserrat",Arial,sans-serif;font-size:9px;color:#777}
.main-nav a{position:absolute;white-space:nowrap;text-decoration:none;color:#777}
.main-nav a.active{color:var(--black);font-weight:500}

/* hero */
.hero-band{left:0;top:66px;width:819px;height:262px;background:var(--green)}
.hero-slider{left:67px;top:98px;width:685px;height:300px;background:var(--white);padding:3px;box-shadow:0 3px 8px rgba(0,0,0,.18)}
.hero-photo{width:100%;height:100%;background:linear-gradient(100deg,#e9ece8 0%,#d8dcd6 35%,#c9c6bd 60%,#e2e1dc 100%)}
.slider-dots{left:382px;top:372px;display:flex;gap:4px}
.slider-dots span{width:10px;height:10px;border-radius:50%;border:1.5px solid var(--white);background:rgba(255,255,255,.35)}

/* welcome */
.welcome-title{left:0;top:425px;width:819px;text-align:center;font-size:14.5px;font-weight:600;color:var(--ink)}
.welcome-title em{font-style:normal;color:var(--green)}
.welcome-copy{left:185px;top:457px;width:450px;text-align:center;font-size:8px;line-height:15.3px}

/* sectors */
.sector{width:150px;text-align:center}
.sector-ring{width:74px;height:74px;margin:0 auto;border-radius:50%;background:radial-gradient(circle at 50% 40%,#b8da45,var(--green-dark));box-shadow:0 9px 10px rgba(0,0,0,.14);display:flex;align-items:center;justify-content:center;color:var(--white);font-family:"Montserrat",Arial,sans-serif;font-size:24px;font-weight:500}
.sector-ring small{font-size:11px;margin-top:8px}
.sector-name{margin-top:14px;height:32px;font-family:"Montserrat",Arial,sans-serif;font-size:11px;font-weight:500;color:#333;line-height:15px}
.sector-copy{margin-top:10px;font-size:7.8px;line-height:13.5px}

/* services */
.services{left:0;top:734px;width:819px;height:230px;background:linear-gradient(90deg,#1a1d20,#2c3238 50%,#1d2024)}
.services-title{left:68px;top:760px;font-size:13px;font-weight:600;color:var(--white)}
.services-title em{font-style:normal;color:var(--green)}
.svc-arrow{width:21px;height:21px;border-radius:50%;border:1px solid #666;top:758px}
.svc-card{top:796px;width:213px;height:134px;box-shadow:0 2px 6px rgba(0,0,0,.3)}
.svc-photo{height:98px;background:linear-gradient(120deg,#dfe3e6,#b9c6d2 55%,#e8ebee)}
.svc-bar{height:36px;background:var(--green);display:flex;align-items:center;justify-content:space-between;padding:0 10px 0 14px;font-family:"Montserrat",Arial,sans-serif;font-size:11px;font-weight:500;color:var(--white)}

/* news */
.news-title{left:65px;top:1001px;font-size:14.5px;font-weight:600;color:var(--ink)}
.news-title em{font-style:normal;color:var(--green)}
.news-item{top:1035px;width:215px}
.news-date{font-family:"Montserrat",Arial,sans-serif;font-size:8.5px;font-weight:500;color:var(--green)}
.news-copy{margin-top:6px;font-size:7px;line-height:12.4px}
.news-copy b{font-weight:400;color:var(--black)}

/* footer */
.site-footer{left:0;top:1134px;width:819px;height:66px;background:var(--green)}
.footer-nav{left:66px;top:1152px;font-family:"Montserrat",Arial,sans-serif;font-size:8px;font-weight:500;color:var(--white);word-spacing:1px}
.footer-legal{left:66px;top:1173px;font-size:7.6px;color:var(--white)}
.social{top:1154px;width:25px;height:25px;border-radius:50%;border:1.5px solid var(--white)}
</style>
</head>
<body>

<header class="abs site-header">
  <div class="abs brand"><span class="brand-dot"></span><span class="brand-name">BrightLane Consultants</span></div>
  <nav class="abs main-nav">
    <a class="active" style="left:0">HOME</a>
    <a style="left:65px">ABOUT US</a>
    <a style="left:149px">SERVICES</a>
    <a style="left:229px">PRODUCTS</a>
    <a style="left:313px">NEWS</a>
    <a style="left:375px">CONTACT US</a>
  </nav>
</header>

<div class="abs hero-band"></div>
<div class="abs hero-slider"><div class="hero-photo" role="img" aria-label="Photo of three colleagues smiling around a laptop in a bright office"></div></div>
<div class="abs slider-dots"><span></span><span></span><span></span><span></span></div>

<h1 class="abs heading welcome-title">WELCOME TO <em>BRIGHTLANE</em></h1>
<p class="abs welcome-copy">Sed quia non numquam eius modi tempora incidunt ut labore et dolore magnam aliquam quaerat voluptatem. Ut enim ad minima veniam, quis nostrum exercitationem ullam corporis suscipit laboriosam, nisi ut aliquid ex ea com-modi consequatur. Neque porro quisquam est, qui dolorem ipsum quia dolor sit amet.</p>

<div class="abs sector" style="left:62px;top:528px">
  <div class="sector-ring">6<small>%</small></div>
  <div class="sector-name">HI-TECH</div>
  <p class="sector-copy">Sed quia non numquam eius modi tempora incidunt ut labore et dolore magnam aliquam quaerat</p>
</div>
<div class="abs sector" style="left:249px;top:528px">
  <div class="sector-ring">15<small>%</small></div>
  <div class="sector-name">HEALTHCARE &amp;<br>CONSUMER/FMCG</div>
  <p class="sector-copy">Sed quia non numquam eius modi tempora incidunt ut labore et dolore magnam aliquam quaerat</p>
</div>
<div class="abs sector" style="left:423px;top:528px">
  <div class="sector-ring">15<small>%</small></div>
  <div class="sector-name">INDUSTRIAL &amp;<br>ENGINEERING</div>
  <p class="sector-copy">Sed quia non numquam eius modi tempora incidunt ut labore et dolore magnam aliquam quaerat</p>
</div>
<div class="abs sector" style="left:606px;top:528px">
  <div class="sector-ring">15<small>%</small></div>
  <div class="sector-name">BANKING &amp;<br>FINANCE</div>
  <p class="sector-copy">Sed quia non numquam eius modi tempora incidunt ut labore et dolore magnam aliquam quaerat</p>
</div>

<section class="abs services" role="img" aria-label="Dark background photo of a business meeting"></section>
<h2 class="abs heading services-title">RECRUITMENT <em>SERVICES</em></h2>
<div class="abs svc-arrow" style="left:703px"><svg width="19" height="19" viewBox="0 0 19 19"><path d="M11 6l-3.5 3.5L11 13" fill="none" stroke="#999" stroke-width="1.2"/></svg></div>
<div class="abs svc-arrow" style="left:730px"><svg width="19" height="19" viewBox="0 0 19 19"><path d="M8 6l3.5 3.5L8 13" fill="none" stroke="#999" stroke-width="1.2"/></svg></div>

<div class="abs svc-card" style="left:67px"><div class="svc-photo" role="img" aria-label="Photo of two men working at a laptop"></div><div class="svc-bar">SED UT PERSPICIATIS<svg width="8" height="10" viewBox="0 0 8 10"><path d="M2 1l4 4-4 4" fill="none" stroke="#fff" stroke-width="1.4"/></svg></div></div>
<div class="abs svc-card" style="left:303px"><div class="svc-photo" role="img" aria-label="Photo of a smiling team in an office"></div><div class="svc-bar">SED UT PERSPICIATIS<svg width="8" height="10" viewBox="0 0 8 10"><path d="M2 1l4 4-4 4" fill="none" stroke="#fff" stroke-width="1.4"/></svg></div></div>
<div class="abs svc-card" style="left:538px"><div class="svc-photo" role="img" aria-label="Photo of two business people talking"></div><div class="svc-bar">SED UT PERSPICIATIS<svg width="8" height="10" viewBox="0 0 8 10"><path d="M2 1l4 4-4 4" fill="none" stroke="#fff" stroke-width="1.4"/></svg></div></div>

<h2 class="abs heading news-title">LATEST <em>NEWS</em></h2>
<article class="abs news-item" style="left:64px"><div class="news-date">March 25-2015</div><p class="news-copy">Lorem ipsum dolor amet, vis te nibh dicret, decoressim et meais ad vrelorei mipsum hadrum elaboraret, elit labore eu nuquam mandamus. <b>Read More</b></p></article>
<article class="abs news-item" style="left:300px"><div class="news-date">March 25-2015</div><p class="news-copy">Lorem ipsum dolor amet, vis te nibh dicret, decoressim et meais ad vrelorei mipsum hadrum elaboraret, elit labore eu nuquam mandamus. <b>Read More</b></p></article>
<article class="abs news-item" style="left:538px"><div class="news-date">March 25-2015</div><p class="news-copy">Lorem ipsum dolor amet, vis te nibh dicret, decoressim et meais ad vrelorei mipsum hadrum elaboraret, elit labore eu nuquam mandamus. <b>Read More</b></p></article>

<footer class="abs site-footer"></footer>
<div class="abs footer-nav">HOME &nbsp;| &nbsp;ABOUT US &nbsp;| &nbsp;SERVICES &nbsp;| &nbsp;PRODUCTS &nbsp;| &nbsp;NEWS &nbsp;| &nbsp;CONTACT US</div>
<div class="abs footer-legal">Disclaimer | Privacy Policy | © 2015 BrightLane all copyrights are reserved</div>
<div class="abs social" style="left:614px"></div>
<div class="abs social" style="left:642px"></div>
<div class="abs social" style="left:670px"></div>
<div class="abs social" style="left:698px"></div>
<div class="abs social" style="left:726px"></div>

</body>
</html>
```